Business Card Design for Property Development Company Director

I am looking for a professional and unforgettable business card design for our Director of our Property Development Company.
Please see attached .pptx file to find out what information to include. You don't have to follow the exact format shown in the file - I am interested to see your creative flair using the information provided.

```html
<!DOCTYPE html>
<html lang="en">
<head>
<meta charset="utf-8">
<title>Halvern Property Group – Business Card</title>
<link href="https://fonts.googleapis.com/css2?family=Roboto:wght@400;500;700;900&display=swap" rel="stylesheet">
<style>
  :root {
    --bg: #3a3b3e;
    --card: #ffffff;
    --blue: #1457a8;
    --grey: #555759;
    --ink: #1b1b1b;
  }
  * { margin: 0; padding: 0; box-sizing: border-box; }
  html, body { width: 1200px; height: 1200px; overflow: hidden; }
  body {
    background: var(--bg);
    font-family: "Roboto", Arial, sans-serif;
    position: relative;
  }
  .card {
    position: absolute;
    left: 150px;
    width: 900px;
    height: 514px;
    background: var(--card);
    border-radius: 34px;
    box-shadow: 0 12px 30px rgba(0,0,0,0.35);
  }
  .card--front { top: 60px; }
  .card--back { top: 626px; }

  /* Front */
  .tagline {
    position: absolute;
    top: 70px; left: 0; right: 0;
    text-align: center;
    color: var(--blue);
    font-weight: 500;
    font-size: 30px;
    line-height: 1.2;
  }
  .brand {
    display: flex;
    align-items: center;
    gap: 18px;
    color: var(--blue);
    font-weight: 900;
  }
  .brand__mark {
    width: 64px; height: 64px;
    background: var(--blue);
    flex: none;
  }
  .brand__name {
    font-size: 52px;
    line-height: 1;
    letter-spacing: 1px;
  }
  .card--front .brand {
    position: absolute;
    top: 210px; left: 0; right: 0;
    justify-content: center;
  }
  .front-note {
    position: absolute;
    bottom: 64px; left: 0; right: 0;
    text-align: center;
    color: var(--grey);
    font-size: 26px;
  }
  .front-note strong { color: var(--blue); font-weight: 500; }

  /* Back */
  .card--back .brand {
    position: absolute;
    top: 150px; left: 60px;
    width: 440px;
    flex-wrap: wrap;
  }
  .card--back .brand__name { font-size: 40px; width: 340px; line-height: 1.1; }
  .divider {
    position: absolute;
    left: 530px; top: 110px;
    width: 2px; height: 200px;
    background: var(--blue);
  }
  .person {
    position: absolute;
    left: 560px; top: 110px;
  }
  .person__name {
    color: var(--blue);
    font-weight: 700;
    font-size: 34px;
  }
  .person__role {
    color: var(--ink);
    font-size: 20px;
    margin-bottom: 26px;
  }
  .contact {
    list-style: none;
    color: var(--ink);
    font-size: 23px;
  }
  .contact li {
    display: flex;
    align-items: center;
    gap: 12px;
    margin-bottom: 8px;
  }
  .contact svg { width: 20px; height: 20px; flex: none; }
  .licence {
    position: absolute;
    bottom: 60px; left: 60px;
    color: var(--grey);
    font-size: 26px;
    font-weight: 500;
  }
  .licence span { color: var(--blue); }
</style>
</head>
<body>

<section class="card card--front">
  <p class="tagline">Property Development<br>&amp; Site Acquisition Specialists</p>
  <div class="brand">
    <span class="brand__mark"></span>
    <span class="brand__name">HALVERN PROPERTY GROUP</span>
  </div>
  <p class="front-note">Ask me about our <strong>INVESTMENT &amp; PARTNERSHIP</strong> opportunities</p>
</section>

<section class="card card--back">
  <div class="brand">
    <span class="brand__mark"></span>
    <span class="brand__name">HALVERN PROPERTY GROUP</span>
  </div>
  <div class="divider"></div>
  <div class="person">
    <h1 class="person__name">Daniel Marsh</h1>
    <p class="person__role">Director</p>
    <ul class="contact">
      <li>
        <svg viewBox="0 0 24 24" fill="#1457a8"><path d="M6.6 10.8a15 15 0 0 0 6.6 6.6l2.2-2.2c.3-.3.7-.4 1-.2 1.1.4 2.3.6 3.6.6.6 0 1 .4 1 1V20c0 .6-.4 1-1 1A17 17 0 0 1 3 4c0-.6.4-1 1-1h3.5c.6 0 1 .4 1 1 0 1.3.2 2.5.6 3.6.1.3 0 .7-.2 1z"/></svg>
        0400 123 456
      </li>
      <li>
        <svg viewBox="0 0 24 24" fill="none" stroke="#1457a8" stroke-width="2"><rect x="3" y="5" width="18" height="14" rx="1"/><path d="M3 6l9 7 9-7"/></svg>
        daniel@halvern.com.au
      </li>
      <li>
        <svg viewBox="0 0 24 24" fill="none" stroke="#1457a8" stroke-width="1.8"><circle cx="12" cy="12" r="9"/><path d="M3 12h18M12 3c3 3 3 15 0 18M12 3c-3 3-3 15 0 18"/></svg>
        www.halvern.com.au
      </li>
    </ul>
  </div>
  <p class="licence">Real Estate Lic: <span>1234567 &amp; 1234568</span></p>
</section>

</body>
</html>
```